PostCard for Managed IT Services

We need a postcard design for a postcard that we intend to send out early in our marketing efforts to medical practices. The postcard should communicate our core services for small businesses including 1.) Managed IT Services, 2.) Security Services, 3.) Cloud Services, and 4.) IT Project and Integration work. company information is available at www.larkfordit.com. I attached a two logos.WHILE WE WANT TO USE THE LOGO AND COLORS FROM OUR SITE, I HOPE THE DESIGN IS BOLD AND GRABS ATTENTION. I HOPE IT IS NOT THE 'SAME OLD' INFORMATION TECHNOLOGY LOOK. BE CREATIVE AND GET THE READER TO LOOK TWICE.

Target Market(s)

Businesses, medical practices

Font styles to use
Serif
Sans Serif

Requirements
Must have
• We need to include somewhere that are technicians are trained in on HIPAA and PCI (see site for info on the two)

```html
<!DOCTYPE html>
<html lang="en">
<head>
<meta charset="utf-8">
<title>Larkford IT – Postcard</title>
<link href="https://fonts.googleapis.com/css2?family=Noto+Serif:wght@400;700&family=Oswald:wght@500&display=swap" rel="stylesheet">
<style>
  :root{
    --blue:#21407f;
    --blue-deep:#1c3670;
    --blue-soft:#5b7cc4;
    --green:#53b048;
    --paper:#f1f2f4;
    --white:#ffffff;
    --ink:#1f2a3a;
    --stage:#e4e5e8;
    --serif:'Noto Serif', Georgia, serif;
    --condensed:'Oswald', 'Arial Narrow', sans-serif;
  }
  *{margin:0;padding:0;box-sizing:border-box}
  html,body{width:849px;height:1200px;overflow:hidden;background:var(--stage)}
  .card{position:absolute;left:22px;width:806px;height:536px;background:var(--paper);overflow:hidden;box-shadow:0 4px 14px rgba(0,0,0,.25)}
  .card--front{top:52px}
  .card--back{top:612px;background:var(--white)}
  .card__art{position:absolute;inset:0}
  .abs{position:absolute}

  /* front */
  .brand{left:0;width:314px;top:82px;text-align:center;font-family:var(--serif);font-weight:700;font-size:28px;letter-spacing:6px;color:var(--blue)}
  .tagline{left:0;width:314px;text-align:center;font-family:var(--serif);font-weight:700;font-size:10px;letter-spacing:6px;color:#4a63b0}
  .tagline--one{top:192px}
  .tagline--two{top:212px}
  .headline{left:22px;top:238px;font-family:var(--serif);font-weight:700;font-size:26px;line-height:36px;color:var(--white)}
  .services-label{left:24px;top:337px;width:233px;height:35px;border-radius:18px;background:var(--green);color:var(--white);font-family:var(--condensed);font-size:24px;line-height:35px;text-align:center;letter-spacing:.3px}
  .service{display:flex;gap:8px;align-items:flex-start;font-family:var(--condensed);font-size:18px;line-height:22px;color:var(--ink)}
  .service svg{margin-top:4px;flex:none}
  .contact{top:489px;display:flex;align-items:center;gap:8px;font-family:var(--serif);font-size:16px;color:var(--white)}
  .web-pill{left:554px;top:452px;width:252px;height:36px;background:var(--green);border-radius:18px 0 0 18px;display:flex;align-items:center;gap:10px;padding-left:20px;font-family:var(--serif);font-size:16px;color:var(--white)}

  /* back */
  .back-title{left:25px;top:18px;font-family:var(--serif);font-weight:700;color:var(--blue)}
  .back-title__main{display:block;font-size:30px;line-height:36px}
  .back-title__sub{display:block;font-size:19px;line-height:24px}
  .back-title__sub em{font-style:normal;color:var(--green)}
  .topic{left:25px;width:390px;color:var(--white)}
  .topic h2{font-family:var(--condensed);font-weight:500;font-size:22px;line-height:27px}
  .topic p{font-family:var(--serif);font-size:15px;line-height:19px;margin-top:8px}
  .topic p + p{margin-top:18px}
  .topic--pci{top:102px}
  .topic--hipaa{top:272px}
  .visit{left:25px;top:490px;font-family:var(--serif);font-weight:700;font-size:19px;letter-spacing:1.5px;color:var(--white)}
  .stamp{left:715px;top:26px;width:63px;height:81px;border:2px solid #111}
</style>
</head>
<body>

<section class="card card--front">
  <svg class="card__art" width="806" height="536" viewBox="0 0 806 536">
    <defs>
      <radialGradient id="photoTone" cx="65%" cy="40%" r="70%">
        <stop offset="0" stop-color="#9aa6b4"/>
        <stop offset=".55" stop-color="#4f5d70"/>
        <stop offset="1" stop-color="#222c3a"/>
      </radialGradient>
    </defs>
    <rect class="headline-band" x="0" y="236" width="330" height="86" fill="var(--blue)"/>
    <rect class="contact-band" x="0" y="474" width="806" height="62" fill="var(--blue)"/>
    <circle cx="706" cy="268" r="360" fill="var(--white)"/>
    <circle cx="706" cy="268" r="336" fill="url(#photoTone)" role="img" aria-label="Photo of a businessman holding out an open hand with floating cloud, database, computer and user icons over a world map"/>
    <path d="M478 0 A352 352 0 0 0 380 136" fill="none" stroke="var(--blue)" stroke-width="12"/>
    <path d="M377 172 A343 343 0 0 0 492 536" fill="none" stroke="var(--green)" stroke-width="14"/>
  </svg>

  <div class="abs brand">Larkford IT</div>
  <div class="abs tagline tagline--one">Managed Services</div>
  <div class="abs tagline tagline--two">Partner with the best!</div>

  <h1 class="abs headline">Partner With The Best<br>For All Your IT Needs</h1>

  <div class="abs services-label">OUR CORE SERVICES</div>

  <div class="abs service" style="left:22px;top:385px">
    <svg width="14" height="14" viewBox="0 0 14 14"><rect x="1" y="1" width="12" height="12" fill="none" stroke="var(--green)" stroke-width="1.6"/><path d="M3.5 7 L6 9.5 L12.5 3" fill="none" stroke="var(--green)" stroke-width="1.8"/></svg>
    <span>Managed IT Services</span>
  </div>
  <div class="abs service" style="left:203px;top:385px">
    <svg width="14" height="14" viewBox="0 0 14 14"><rect x="1" y="1" width="12" height="12" fill="none" stroke="var(--green)" stroke-width="1.6"/><path d="M3.5 7 L6 9.5 L12.5 3" fill="none" stroke="var(--green)" stroke-width="1.8"/></svg>
    <span>Cloud Services</span>
  </div>
  <div class="abs service" style="left:22px;top:433px">
    <svg width="14" height="14" viewBox="0 0 14 14"><rect x="1" y="1" width="12" height="12" fill="none" stroke="var(--green)" stroke-width="1.6"/><path d="M3.5 7 L6 9.5 L12.5 3" fill="none" stroke="var(--green)" stroke-width="1.8"/></svg>
    <span>Security Services</span>
  </div>
  <div class="abs service" style="left:203px;top:421px">
    <svg width="14" height="14" viewBox="0 0 14 14"><rect x="1" y="1" width="12" height="12" fill="none" stroke="var(--green)" stroke-width="1.6"/><path d="M3.5 7 L6 9.5 L12.5 3" fill="none" stroke="var(--green)" stroke-width="1.8"/></svg>
    <span>IT Project and<br>Integration work</span>
  </div>

  <div class="abs contact" style="left:24px">
    <svg width="18" height="18" viewBox="0 0 24 24"><path d="M6.6 10.8a15.1 15.1 0 0 0 6.6 6.6l2.2-2.2a1 1 0 0 1 1-.25 11.4 11.4 0 0 0 3.6.57 1 1 0 0 1 1 1V20a1 1 0 0 1-1 1A17 17 0 0 1 3 4a1 1 0 0 1 1-1h3.5a1 1 0 0 1 1 1c0 1.25.2 2.45.57 3.57a1 1 0 0 1-.25 1z" fill="var(--green)"/></svg>
    <span>(555) 014-2287</span>
  </div>
  <div class="abs contact" style="left:182px">
    <svg width="20" height="15" viewBox="0 0 20 15"><rect x="0" y="0" width="20" height="15" rx="1.5" fill="var(--green)"/><path d="M1 1 L10 8.5 L19 1" fill="none" stroke="var(--blue)" stroke-width="1.6"/></svg>
    <span>info@larkfordit.com</span>
  </div>

  <div class="abs web-pill">
    <svg width="17" height="17" viewBox="0 0 20 20" fill="none" stroke="var(--white)" stroke-width="1.4"><circle cx="10" cy="10" r="8.5"/><ellipse cx="10" cy="10" rx="4" ry="8.5"/><path d="M1.5 10h17M3 5.5h14M3 14.5h14"/></svg>
    <span>www.larkfordit.com</span>
  </div>
</section>

<section class="card card--back">
  <svg class="card__art" width="806" height="536" viewBox="0 0 806 536">
    <defs>
      <linearGradient id="panelTone" x1="0" y1="0" x2="1" y2="0">
        <stop offset="0" stop-color="#2a4688"/>
        <stop offset="1" stop-color="var(--blue-soft)"/>
      </linearGradient>
      <clipPath id="backArc"><circle cx="81" cy="268" r="346"/></clipPath>
    </defs>
    <rect x="0" y="0" width="440" height="88" fill="var(--paper)" clip-path="url(#backArc)"/>
    <g clip-path="url(#backArc)">
      <rect class="info-panel" x="0" y="88" width="440" height="384" fill="url(#panelTone)"/>
      <rect class="visit-band" x="0" y="474" width="440" height="62" fill="var(--green)"/>
    </g>
    <path d="M333 0 A368 368 0 0 1 425 136" fill="none" stroke="var(--blue)" stroke-width="12"/>
    <path d="M439 168 A372 372 0 0 1 436 380" fill="none" stroke="var(--green)" stroke-width="12"/>
  </svg>

  <h1 class="abs back-title">
    <span class="back-title__main">Our Technicians Are</span>
    <span class="back-title__sub">Trained in on <em>HIPAA and PCI</em></span>
  </h1>

  <article class="abs topic topic--pci">
    <h2>Payment Card Industry Data<br>Security Standards (PCI DSS)</h2>
    <p>The technicians at Larkford IT know the PCI DSS Compliance regulations very well and can answer most your questions regarding it. We typically setup networks with these standards in mind!</p>
  </article>

  <article class="abs topic topic--hipaa">
    <h2>Health Insurance Portability<br>Accountability Act (HIPAA)</h2>
    <p>The team at Larkford IT are well versed with the law and proper ways to safeguard your PHI.</p>
    <p>All workstations and servers that we install are encrypted and we take every possible measure to keep your data safe!</p>
  </article>

  <div class="abs visit">Visit us www.larkfordit.com</div>

  <div class="abs stamp"></div>
</section>

</body>
</html>
```